Company letter head

Hello,
We are a global logistics company requiring a letterhead design for all our company documentation.
Company Name: Clearly display the full name of your company at the top of the letterhead.
Logo: Include your company logo for brand recognition.
Contact Information: This includes your company's address, phone number, email address, and website URL.
Target Market(s)
Clients/customers
Industry/Entity Type
Logistics
Font styles to use
Sans Serif
Requirements
Must have
- Company name and logo
Nice to have
- borders, header/footers

```html
<!DOCTYPE html>
<html lang="en">
<head>
<meta charset="utf-8">
<title>Northwind Freight Ltd – Letterhead</title>
<link href="https://fonts.googleapis.com/css2?family=Roboto:wght@500;700&family=Lato:wght@400&family=Montserrat:wght@400;600&family=Questrial&family=Open+Sans:wght@600&display=swap" rel="stylesheet">
<style>
  :root {
    --brand-red: #d71f26;
    --ink-dark: #3b3b3d;
    --ink-mid: #5c5c5e;
    --ink-light: #9a9a9c;
    --body-text: #a3a3a5;
    --paper: #ffffff;
    --backdrop: #ecedef;
    --footer-band: #3d3d3f;
  }
  * { margin: 0; padding: 0; box-sizing: border-box; }
  html, body { width: 1068px; height: 1200px; overflow: hidden; background: var(--backdrop); }
  .letterhead {
    position: absolute; left: 106px; top: 0;
    width: 855px; height: 1200px;
    background: var(--paper); overflow: hidden;
  }
  .brand-mark {
    position: absolute; left: 53px; top: 84px;
    display: flex; align-items: center; gap: 10px;
    font-family: "Roboto", sans-serif; font-weight: 700;
    font-size: 24px; color: var(--brand-red);
  }
  .brand-mark .brand-square { width: 18px; height: 18px; background: var(--brand-red); }
  .company-block {
    position: absolute; right: 50px; top: 48px; text-align: right;
  }
  .company-name {
    font-family: "Roboto", sans-serif; font-weight: 500;
    font-size: 23px; color: var(--brand-red); line-height: 1.2;
  }
  .company-address {
    font-family: "Lato", sans-serif; font-size: 14.5px;
    color: var(--ink-mid); line-height: 17px; margin-top: 3px;
  }
  .recipient { position: absolute; left: 53px; top: 288px; font-family: "Montserrat", sans-serif; }
  .recipient-name { font-weight: 600; font-size: 21px; color: var(--ink-dark); letter-spacing: .3px; }
  .recipient-line { font-size: 14.5px; color: var(--ink-light); margin-top: 8px; line-height: 20px; white-space: nowrap; }
  .letter-date {
    position: absolute; right: 50px; top: 406px;
    font-family: "Open Sans", sans-serif; font-weight: 600;
    font-size: 17px; color: var(--ink-light);
  }
  .letter-body {
    position: absolute; left: 53px; top: 450px; width: 753px;
    font-family: "Questrial", sans-serif; font-size: 16.3px;
    line-height: 26.5px; color: var(--body-text); text-align: justify;
    hyphens: manual;
  }
  .letter-body p + p { margin-top: 26.5px; }
  .sign-off {
    position: absolute; left: 67px; top: 866px;
    font-family: "Montserrat", sans-serif; font-weight: 600;
    font-size: 26px; color: var(--ink-dark);
  }
  .signature-area {
    position: absolute; left: 94px; top: 912px; width: 122px; height: 75px;
    background: linear-gradient(135deg, #f1f1f1, #e4e4e4);
  }
  .footer-band {
    position: absolute; left: 0; top: 1133px; width: 563px; height: 29px;
    background: var(--footer-band); z-index: 2;
    display: flex; align-items: center; padding-left: 38px; gap: 14px;
    font-family: "Lato", sans-serif; font-size: 14px; color: #fff;
    white-space: nowrap;
  }
  .contact-item { display: flex; align-items: center; gap: 6px; white-space: nowrap; }
  .contact-icon {
    flex: none;
    width: 15px; height: 15px; background: var(--brand-red);
    display: flex; align-items: center; justify-content: center;
  }
  .corner-illustration {
    position: absolute; right: 0; bottom: 0; width: 318px; height: 189px; z-index: 1;
    border-top-left-radius: 160px 189px;
    background: linear-gradient(160deg, #e23a40 0%, var(--brand-red) 45%, #4a4a4c 100%);
  }
</style>
</head>
<body>
<main class="letterhead">
  <div class="brand-mark"><span class="brand-square"></span>Northwind Freight</div>

  <header class="company-block">
    <h1 class="company-name">Northwind Freight Ltd</h1>
    <p class="company-address">72 Harbor View Rd. Suite 5<br>Baltimore, MD 21230</p>
  </header>

  <section class="recipient">
    <h2 class="recipient-name">ALDEN MARSH</h2>
    <p class="recipient-line">0198-555-214</p>
    <p class="recipient-line">alden@northwindfreight.example</p>
    <p class="recipient-line">415 Dockside Ave. Suite<br>8 Portland, OR 97201</p>
  </section>

  <p class="letter-date">12 December, 2024</p>

  <article class="letter-body">
    <p>Lorem ipsum dolor sit amet, consectetuer adipiscing elit, sed diam nonummy nibh euismod tincidunt ut laoreet dolore magna aliquam erat volutpat. Ut wisi enim ad minim veniam, quis nostrud exerci tation ullamcorper suscipit lobortis nisl ut aliquip ex ea commodo consequat. Duis autem vel eum iriure dolor in hendrerit in vulputate velit esse molestie consequat, vel illum dolore eu feugiat nulla fac&shy;ilisis at vero eros et accumsan et iusto odio dignissim qui blandit praesent luptatum zzril delenit augue duis dolore te feugait nulla facilisi.</p>
    <p>Lorem ipsum dolor sit amet, cons ectetuer adipiscing elit, sed diam nonummy nibh euismod tincidunt ut laoreet dolore magna aliquam erat volutpat. Ut wisi enim ad minim veniam, quis nostrud exerci tation ullamcorper suscipit lobortis nisl ut aliquip ex ea commodo consequat.</p>
    <p>Lorem ipsum dolor sit amet, consectetuer adipiscing elit, sed diam nonummy nibh euismod tincidunt ut laoreet dolore magna aliquam erat</p>
  </article>

  <p class="sign-off">Mr. Alden Marsh</p>
  <div class="signature-area" role="img" aria-label="Handwritten signature"></div>

  <div class="corner-illustration" role="img" aria-label="Illustration of a globe with a cargo ship, containers, aeroplane and road"></div>

  <footer class="footer-band">
    <span class="contact-item">
      <span class="contact-icon"><svg width="10" height="10" viewBox="0 0 24 24"><path fill="#fff" d="M6.6 10.8a15 15 0 0 0 6.6 6.6l2.2-2.2c.3-.3.7-.4 1-.2 1.1.4 2.3.6 3.6.6.6 0 1 .4 1 1V20c0 .6-.4 1-1 1A17 17 0 0 1 3 4c0-.6.4-1 1-1h3.5c.6 0 1 .4 1 1 0 1.3.2 2.5.6 3.6.1.3 0 .7-.2 1z"/></svg></span>
      01632 96 04 17
    </span>
    <span class="contact-item">
      <span class="contact-icon"><svg width="11" height="9" viewBox="0 0 22 16"><rect x="1" y="1" width="20" height="14" fill="none" stroke="#fff" stroke-width="2"/><path d="M1 1l10 8 10-8" fill="none" stroke="#fff" stroke-width="2"/></svg></span>
      hello@northwind.example
    </span>
    <span class="contact-item">
      <span class="contact-icon"><svg width="9" height="11" viewBox="0 0 18 22"><path fill="#fff" d="M2 1l14 12-6 1 4 7-3 1-4-7-5 4z"/></svg></span>
      www.northwind.example
    </span>
  </footer>
</main>
</body>
</html>
```